Packaging design for aloe lotion bottle for a Laser Clinic

We need a packaging design for a body lotion bottle. Our business is a laser clinic and we are looking at slowly rolling out a range of skincare products. This lotion bottle is the first item with more to follow so the winning designer will have other designs to work on in the future.

The design needs to be classy, elegant, strong and sophisticated. The bottle will be clear with a shiny silver sleeved lid. The lotion itself, which will be visible through the bottle, will be a very light green colour. Think Mirelle Davonne and Voriel as that is the image I want to convey.

Ideally we were thinking of having a design with a single colour but if you come up with a fantastic multi colour design that we love then we're open to it.

Reason: I have extended the deadline as I feel I need more time to allow designers to submit their designs. I haven't found a design that I love just yet. The project has been made a guaranteed payment upon completion. Thank you.

Target Market(s)

upper class high income earners with a high disposable income. People that look after themselves

Industry/Entity Type

Beauty Salon

Colors
000000
cadf82

Requirements
Must have
• must include the details below:
• Post Laser Calming Cream
• This soothing and calming anti inflammatory cream is specifically formulated for use after post laser treatments.
• Fresh Cucumber, Melon and Aloe Vera Leaf Juice blend together in perfect harmony to quickly cool you skin and restore your skins natural moisture.
• Our luxurious calming cream targets redness and helps to reduce inflammation, bringing you supple and radiant skin like never before.
• Directions: Use a liberal amount twice daily on all your treatment areas. This nourishing cream can also be used daily to restore moisture and softness to areas of the face and body not being treated by laser or IPL.
• Ingredients: water (aqua), glycine soja (soybean) oil, cetyl alcohol, glycerin dimethicone, butyrospermum parkii (shea butter), theobroma cacao (cocoa) seed butter, aloe barbadensis (aloe vera) leaf juice, tocopheryl acetate, sodium ascorbyl phosphate, disodium EDTA, ceteareth-20, carbomer, BHT, benzyl benzoate, butylphenyl methylpropional, hexyl cinnamal, linalool, glyceryl caprylate, methylisothiazolinone. May contain: Red 4 (CI 14700, aka 504), Yellow 5 (CI 19140, Ki4), Yellow 6 (CI 15985, KI5), Blue 1 (CI 42090, Ao1), Red 33 (CI 17200, Aka 227), Ext. Violet 2 (CI 60730, Murasaki401), Green 3 (CI 42053, Midori3)
• Against Animal Testing
• Manufactured in Australia
• www.velvetglowclinic.com.au
• 500ml
• Pure Halo Laser Hair Removal logo (see attached files)
Nice to have
• A sophisticated and elegant design
Should not have
• no photos. not too many different colours

```html
<!DOCTYPE html>
<html lang="en">
<head>
<meta charset="utf-8">
<title>Pure Halo – Post Laser Calming Cream Label</title>
<link rel="stylesheet" href="https://fonts.googleapis.com/css2?family=Montserrat:wght@400;500&family=Saira+Condensed:wght@200;400;500;700&display=swap">
<style>
  :root {
    --label-bg: #f0f0f1;
    --ink: #111111;
    --ink-soft: #333333;
  }
  html, body {
    margin: 0;
    padding: 0;
    width: 1200px;
    height: 1200px;
    overflow: hidden;
    background: var(--label-bg);
  }
  .label {
    position: relative;
    width: 1200px;
    height: 1200px;
    font-family: "Saira Condensed", "Arial Narrow", sans-serif;
    color: var(--ink);
  }
  .label > * {
    position: absolute;
    margin: 0;
  }
  .brand-name {
    left: 236px;
    top: 48px;
    width: 728px;
    font-family: "Montserrat", sans-serif;
    font-size: 108px;
    font-weight: 500;
    letter-spacing: -0.01em;
    line-height: 1;
    text-align: center;
  }
  .brand-tagline {
    left: 236px;
    top: 166px;
    width: 728px;
    font-family: "Montserrat", sans-serif;
    font-size: 38px;
    font-weight: 400;
    letter-spacing: 0.2em;
    line-height: 1;
    text-align: center;
  }
  .description {
    left: 236px;
    top: 250px;
    width: 728px;
    font-size: 18px;
    font-weight: 400;
    line-height: 24px;
    color: var(--ink-soft);
  }
  .description p { margin: 0 0 6px; }
  .product-kicker {
    left: 236px;
    top: 426px;
    font-size: 90px;
    font-weight: 700;
    line-height: 1;
  }
  .product-name {
    left: 232px;
    top: 520px;
    font-size: 128px;
    font-weight: 200;
    letter-spacing: 0.01em;
    line-height: 1;
  }
  .product-benefit {
    left: 236px;
    top: 654px;
    font-size: 50px;
    font-weight: 500;
    letter-spacing: 0.3em;
    line-height: 1;
  }
  .scent {
    left: 0;
    width: 1200px;
    top: 748px;
    display: flex;
    flex-direction: column;
    align-items: center;
  }
  .scent-top { font-size: 38px; font-weight: 500; line-height: 1; }
  .scent-main { font-size: 118px; font-weight: 700; line-height: 0.95; }
  .scent-bottom { font-size: 30px; font-weight: 500; line-height: 1; }
  .fine-print {
    left: 100px;
    top: 948px;
    width: 1000px;
    color: var(--ink-soft);
  }
  .directions {
    margin: 0 0 8px;
    font-size: 15px;
    line-height: 19px;
  }
  .ingredients {
    margin: 0;
    font-size: 14px;
    line-height: 18px;
  }
  .fine-print strong { font-weight: 700; color: var(--ink); }
  .footer {
    left: 100px;
    top: 1124px;
    width: 1000px;
    display: grid;
    grid-template-columns: 1fr auto 1fr;
    align-items: center;
    font-size: 18px;
    font-weight: 500;
  }
  .footer .claims { text-align: left; }
  .footer .volume { font-size: 40px; text-align: center; line-height: 1; }
  .footer .website { text-align: right; }
</style>
</head>
<body>
  <main class="label">
    <p class="brand-name">PURE HALO</p>
    <p class="brand-tagline">LASER HAIR REMOVAL</p>

    <div class="description">
      <p>This soothing and calming anti inflammatory cream is specifically formulated for use after post laser treatments.</p>
      <p>Fresh Cucumber, Melon and Aloe Vera Leaf Juice blend together in perfect harmony to quickly cool your skin and restore your skin's natural moisture.</p>
      <p>Our luxurious calming cream targets redness and helps to reduce inflammation, bringing you supple and radiant skin like never before.</p>
    </div>

    <h1 class="product-kicker">POST LASER</h1>
    <h2 class="product-name">CALMING CREAM</h2>
    <p class="product-benefit">SOOTHING AND CALMING</p>

    <div class="scent">
      <span class="scent-top">Fresh Cucumber</span>
      <span class="scent-main">MELON</span>
      <span class="scent-bottom">Aloe Vera Leaf Juice</span>
    </div>

    <div class="fine-print">
      <p class="directions"><strong>Directions:</strong> Use a liberal amount twice daily on all your treatment areas. This nourishing cream can also be used daily to restore moisture and softness to areas of the face and body not being treated by laser or IPL.</p>
      <p class="ingredients"><strong>Ingredients:</strong> water (aqua), glycine soja (soybean) oil, cetyl alcohol, glycerin dimethicone, butyrospermum parkii (shea butter), theobroma cacao (cocoa) seed butter, aloe barbadensis (aloe vera) leaf juice, tocopheryl acetate, sodium ascorbyl phosphate, disodium EDTA, ceteareth-20, carbomer, BHT, benzyl benzoate, butylphenyl methylpropional, hexyl cinnamal, linalool, glyceryl caprylate, methylisothiazolinone. May contain: Red 4 (CI 14700, aka 504), Yellow 5 (CI 19140, Ki4), Yellow 6 (CI 15985, KI5), Blue 1 (CI 42090, Ao1), Red 33 (CI 17200, Aka 227), Ext. Violet 2 (CI 60730, Murasaki401), Green 3 (CI 42053, Midori3)</p>
    </div>

    <div class="footer">
      <span class="claims">Against Animal Testing · Manufactured in Australia</span>
      <span class="volume">500ml</span>
      <span class="website">www.velvetglowclinic.com.au</span>
    </div>
  </main>
</body>
</html>
```